International Honeymoon Tour Operator needs Business Card

We need to design a business card including our new logo for a new tour operator called Marisol Fenwick Holidays. We would like to also include the text 'Personal Tailor-Made Honeymoons for our Guests at a Lower Cost'. Please Include the following details as well; 'Website: www.marisolfenwickholidays.co.uk'; 'E-mail: tobias@marisolfenwickholidays.co.uk'; 'Mobile: 07914266058'. We would like the design to be compatible with the logo and text. The final design should communicate professionalism, modern and ethical.

We want to business card to be double sided.

We would like to be able to easily adjust the e-mail address and contact number in the future for other employees either through you or ourselves.

Target Market(s)

Brides and grooms aged 18-35 predominantly.

Industry/Entity Type

Business

Colors

Designer to choose colors to be used in the design.

Requirements
Must have
• Logo
Requested Text
Double sided
Nice to have
• Additional colour
The wow factor
Should not have
• Images of currency

```html
<!DOCTYPE html>
<html lang="en">
<head>
<meta charset="utf-8">
<title>Marisol Fenwick Holidays – Business Card</title>
<link rel="stylesheet" href="https://fonts.googleapis.com/css2?family=Questrial&family=Tinos:ital@1&family=Arimo&display=swap">
<style>
  :root {
    --page: #ececea;
    --sage: #d3e2cf;
    --teal: #5a8278;
    --teal-dark: #2f5f5a;
    --lime: #8cc63f;
    --white: #ffffff;
    --rim: #e4e7e3;
    --stitch: #d6dbd5;
  }
  * { margin: 0; padding: 0; box-sizing: border-box; }
  html, body { width: 1200px; height: 1058px; overflow: hidden; background: var(--page); }
  .sheet { position: relative; width: 1200px; height: 1058px; }
  .card {
    position: absolute; left: 180px; width: 840px; height: 480px;
    background: var(--sage); overflow: hidden;
    box-shadow: 0 4px 14px rgba(0,0,0,0.12);
  }
  .card--front { top: 29px; }
  .card--back { top: 549px; }
  .band { position: absolute; left: 0; right: 0; top: 250px; height: 170px; background: var(--teal); }
  .heart { position: absolute; }
  .heart svg { display: block; width: 100%; height: 100%; }
  .heart--front { left: 270px; top: 20px; width: 300px; height: 270px; }
  .heart--back { left: 200px; top: 42px; width: 440px; height: 396px; }
  .brand {
    position: absolute; left: 270px; top: 82px; width: 300px;
    display: flex; flex-direction: column; align-items: center; gap: 10px;
    font-family: "Questrial", sans-serif; color: var(--teal-dark);
  }
  .brand__dot { width: 22px; height: 22px; border-radius: 50%; background: var(--teal-dark); }
  .brand__name { font-size: 28px; line-height: 1.1; text-align: center; }
  .tagline {
    position: absolute; left: 0; right: 0; top: 304px;
    font-family: "Tinos", serif; font-style: italic; font-size: 27px; line-height: 1.2;
    color: var(--white); text-align: center;
  }
  .contacts {
    position: absolute; left: 200px; top: 110px; width: 440px;
    text-align: center; font-family: "Arimo", sans-serif;
  }
  .contact__label { font-family: "Questrial", sans-serif; font-size: 36px; line-height: 1; color: var(--lime); }
  .contact__value { font-size: 16px; line-height: 1.3; color: var(--teal-dark); margin-bottom: 12px; }
</style>
</head>
<body>
<main class="sheet">
  <section class="card card--front" aria-label="Card front">
    <div class="band"></div>
    <div class="heart heart--front">
      <svg viewBox="0 0 200 180" aria-hidden="true">
        <path d="M100 176 C60 142 4 102 4 55 C4 24 28 4 55 4 C78 4 92 17 100 31 C108 17 122 4 145 4 C172 4 196 24 196 55 C196 102 140 142 100 176 Z" fill="var(--rim)"/>
        <path d="M100 166 C64 135 13 98 13 56 C13 30 33 13 56 13 C77 13 91 26 100 40 C109 26 123 13 144 13 C167 13 187 30 187 56 C187 98 136 135 100 166 Z" fill="var(--white)" stroke="var(--stitch)" stroke-width="1" stroke-dasharray="2 2"/>
      </svg>
    </div>
    <div class="brand">
      <span class="brand__dot"></span>
      <span class="brand__name">Marisol Fenwick<br>Holidays</span>
    </div>
    <p class="tagline">Personal Tailor-Made Honeymoons for<br>our Guests at a Lower Cost</p>
  </section>

  <section class="card card--back" aria-label="Card back">
    <div class="heart heart--back">
      <svg viewBox="0 0 200 180" aria-hidden="true">
        <path d="M100 176 C60 142 4 102 4 55 C4 24 28 4 55 4 C78 4 92 17 100 31 C108 17 122 4 145 4 C172 4 196 24 196 55 C196 102 140 142 100 176 Z" fill="var(--rim)"/>
        <path d="M100 168 C64 136 11 98 11 56 C11 29 32 11 56 11 C77 11 91 24 100 38 C109 24 123 11 144 11 C168 11 189 29 189 56 C189 98 136 136 100 168 Z" fill="var(--white)" stroke="var(--stitch)" stroke-width="0.8" stroke-dasharray="1.6 1.6"/>
      </svg>
    </div>
    <div class="contacts">
      <p class="contact__label">Website</p>
      <p class="contact__value">www.marisolfenwickholidays.co.uk</p>
      <p class="contact__label">Email</p>
      <p class="contact__value">tobias@marisolfenwickholidays.co.uk</p>
      <p class="contact__label">Mobile</p>
      <p class="contact__value">+44 (0)7914266058</p>
    </div>
  </section>
</main>
</body>
</html>
```